Brindle Wealth Management Flow Charts

I need help creating three flow charts for my businesses website. We want them to be simple but look professional. This is for a Wealth Management firm. I will attach a word document that has all of the descriptions for everything so you know what icons to use. We just want the chart to have an icon, the names of each step and the corresponding numbers. I will also include some examples of charts we liked as well. Once the winner is selected, we will need help with additional graphic design elements for our website ASAP.
Other font styles liked:
- Goudy Roman

```html
<!DOCTYPE html>
<html lang="en">
<head>
<meta charset="utf-8">
<title>The Retirement Planning Process</title>
<link rel="stylesheet" href="https://fonts.googleapis.com/css2?family=Sorts+Mill+Goudy&family=Oswald:wght@500&display=swap">
<style>
  :root {
    --paper: #f2f2f2;
    --ink: #4a4a4a;
    --line: #555555;
    --icon-light: #f3d9d3;
    --icon-mid: #e9a394;
    --step-1: #1b2438;
    --step-2: #6e353b;
    --step-3: #e0534a;
    --step-4: #ea8a7b;
    --step-5: #f1b3a3;
    --step-6: #e9dcba;
  }
  html, body {
    margin: 0;
    padding: 0;
    overflow: hidden;
  }
  .canvas {
    position: relative;
    width: 1200px;
    height: 982px;
    background: var(--paper);
    overflow: hidden;
  }
  .process-title {
    position: absolute;
    left: 62px;
    top: 36px;
    margin: 0;
    font-family: "Sorts Mill Goudy", Georgia, serif;
    font-weight: 400;
    font-size: 70px;
    line-height: 80px;
    letter-spacing: 1px;
    color: var(--ink);
  }
  .process-graphic {
    position: absolute;
    left: 0;
    top: 0;
  }
  .step-icon {
    position: absolute;
    width: 130px;
    height: 130px;
    border: 1.5px solid var(--line);
    border-radius: 50%;
    background: radial-gradient(circle at 40% 45%, var(--icon-mid) 0%, var(--icon-light) 55%, var(--paper) 100%);
  }
  .icon-discovery { left: 99px;  top: 410px; }
  .icon-planning  { left: 413px; top: 410px; }
  .icon-alignment { left: 736px; top: 410px; }
  .icon-learning  { left: 250px; top: 783px; }
  .icon-execution { left: 570px; top: 783px; }
  .icon-review    { left: 896px; top: 783px; }
  .step-label {
    position: absolute;
    margin: 0;
    font-family: "Oswald", "Arial Narrow", sans-serif;
    font-weight: 500;
    font-size: 27px;
    line-height: 40px;
    letter-spacing: 0.5px;
    color: var(--ink);
    text-transform: uppercase;
  }
  .step-label .indent { padding-left: 26px; }
  .label-discovery { left: 202px; top: 553px; }
  .label-planning  { left: 512px; top: 553px; }
  .label-alignment { left: 832px; top: 553px; }
  .label-learning  { left: 347px; top: 715px; }
  .label-execution { left: 664px; top: 715px; }
  .label-review    { left: 995px; top: 715px; }
</style>
</head>
<body>
<main class="canvas">
  <h1 class="process-title">The Retirement<br>Planning Process</h1>

  <svg class="process-graphic" width="1200" height="982" viewBox="0 0 1200 982" aria-hidden="true">
    <line x1="64" y1="238" x2="1012" y2="238" stroke="var(--line)" stroke-width="1.5"/>
    <line x1="64" y1="255" x2="1012" y2="255" stroke="#9a9a9a" stroke-width="1.2" stroke-dasharray="1.5 4"/>

    <g class="timeline-bar">
      <polygon points="881,658 1044,658 1044,680 881,680" fill="var(--step-6)"/>
      <polygon points="718,658 881,658 893,669 881,680 718,680" fill="var(--step-5)"/>
      <polygon points="555,658 718,658 730,669 718,680 555,680" fill="var(--step-4)"/>
      <polygon points="392,658 555,658 567,669 555,680 392,680" fill="var(--step-3)"/>
      <polygon points="229,658 392,658 404,669 392,680 229,680" fill="var(--step-2)"/>
      <polygon points="66,658 229,658 241,669 229,680 66,680" fill="var(--step-1)"/>
    </g>

    <g class="connectors" stroke="var(--line)" stroke-width="1.5">
      <line x1="165" y1="542" x2="165" y2="658"/>
      <line x1="479" y1="542" x2="479" y2="658"/>
      <line x1="802" y1="542" x2="802" y2="658"/>
      <line x1="316" y1="680" x2="316" y2="783"/>
      <line x1="636" y1="680" x2="636" y2="783"/>
      <line x1="962" y1="680" x2="962" y2="783"/>
    </g>
  </svg>

  <div class="step-icon icon-discovery" role="img" aria-label="Icon for the discovery meeting step"></div>
  <div class="step-icon icon-planning" role="img" aria-label="Icon for the planning step"></div>
  <div class="step-icon icon-alignment" role="img" aria-label="Icon for the alignment step"></div>
  <div class="step-icon icon-learning" role="img" aria-label="Icon for the learning step"></div>
  <div class="step-icon icon-execution" role="img" aria-label="Icon for the execution step"></div>
  <div class="step-icon icon-review" role="img" aria-label="Icon for the review step"></div>

  <p class="step-label label-discovery">1. Discovery<br><span class="indent">Meeting</span></p>
  <p class="step-label label-planning">3. Planning</p>
  <p class="step-label label-alignment">5. Alignment</p>
  <p class="step-label label-learning">2. Learning</p>
  <p class="step-label label-execution">4. Execution</p>
  <p class="step-label label-review">6. Review</p>
</main>
</body>
</html>
```